"Harrow Crest Builders" is a residential building company and needs a new business card design and may re

We would like a redesign based on the existing logo, and would like to see a new font as well. We are bespoke home builders who build sustainable energy efficient homes.

Industry/Entity Type

Construction

Contact Information for Business Card

Business card size 40mm x 90mm

Colors

Designer to choose colors to be used in the design.

```html
<!DOCTYPE html>
<html lang="en">
<head>
<meta charset="utf-8">
<title>Harrow Crest Builders – Business Card</title>
<link href="https://fonts.googleapis.com/css2?family=Ubuntu:wght@500;700&family=Arimo:wght@400;700&display=swap" rel="stylesheet">
<style>
  :root {
    --gold: #927a33;
    --gold-text: #8f762f;
    --paper: #f3f3f3;
    --ink-grey: #6b6b6b;
    --white: #ffffff;
    --backdrop: #3b3b3b;
  }
  * { margin: 0; padding: 0; box-sizing: border-box; }
  html, body { width: 1200px; height: 960px; overflow: hidden; }
  body { background: var(--backdrop); position: relative; font-family: "Arimo", Arial, sans-serif; }

  .card { position: absolute; left: 270px; width: 660px; }
  .card-front { top: 73px; height: 377px; background: var(--gold); }
  .card-back { top: 510px; height: 375px; background: var(--paper); }

  .brand-name {
    font-family: "Ubuntu", sans-serif;
    font-weight: 500;
    text-align: center;
    line-height: 1.05;
  }
  .card-front .brand-name {
    position: absolute; left: 0; right: 0; top: 190px;
    color: var(--white); font-size: 50px;
  }
  .registration {
    position: absolute; left: 0; right: 0; top: 330px;
    text-align: center; color: var(--white);
    font-weight: 700; font-size: 15px;
  }

  .card-back .brand-name {
    position: absolute; left: 50px; width: 240px; top: 140px;
    color: var(--gold-text); font-size: 38px;
  }
  .contact { position: absolute; left: 359px; top: 92px; color: var(--ink-grey); font-size: 15px; }
  .contact-name {
    font-family: "Ubuntu", sans-serif; font-weight: 700;
    color: var(--gold-text); font-size: 19px; letter-spacing: 0.3px;
  }
  .contact-rule { width: 36px; height: 2px; background: var(--gold); margin: 15px 0 20px; }
  .address { line-height: 22px; margin-bottom: 13px; }
  .contact-list { list-style: none; line-height: 21px; }
  .contact-list li { display: flex; align-items: center; gap: 9px; }
  .contact-list svg { width: 14px; height: 14px; flex: none; }
</style>
</head>
<body>
  <section class="card card-front">
    <div class="brand-name">Harrow Crest Builders</div>
    <p class="registration">Registration 30417 ABN: 52 604 913 287</p>
  </section>

  <section class="card card-back">
    <div class="brand-name">Harrow Crest<br>Builders</div>
    <div class="contact">
      <h1 class="contact-name">DANIEL FERRARO</h1>
      <div class="contact-rule"></div>
      <p class="address">PO Box 2187 Eastgate<br>LPO Kelmscott WA 6111</p>
      <ul class="contact-list">
        <li>
          <svg viewBox="0 0 14 14" aria-hidden="true"><path d="M1 5 Q7 1 13 5 L11 6.5 L9 5.5 L9 4.5 Q7 4 5 4.5 L5 5.5 L3 6.5 Z M3 7.5 H11 L12 12 H2 Z" fill="var(--gold)"/></svg>
          0400 555 318
        </li>
        <li>
          <svg viewBox="0 0 14 14" aria-hidden="true"><rect x="1" y="3" width="12" height="8.5" fill="none" stroke="var(--gold)" stroke-width="1.3"/><path d="M1 3 L7 8 L13 3" fill="none" stroke="var(--gold)" stroke-width="1.3"/></svg>
          daniel@harrowcrestbuilders.com.au
        </li>
        <li>
          <svg viewBox="0 0 14 14" aria-hidden="true"><g fill="none" stroke="var(--gold)" stroke-width="1.2"><circle cx="7" cy="7" r="5.8"/><ellipse cx="7" cy="7" rx="2.5" ry="5.8"/><path d="M1.2 7 H12.8 M2 4 H12 M2 10 H12"/></g></svg>
          www.harrowcrestbuilders.com.au
        </li>
      </ul>
    </div>
  </section>
</body>
</html>
```